Design the Keystone HR business card for my new business

I've just had a logo designed (attached) for my new business doing HR consulting. I'm a one person operation at this stage, my aim is to provide support and help to small to medium sized businesses with their people objectives or issues.

I'm not really into anything overly flashy, I'm not a PR or marketing agency. I'd like my card to look modern, professional and not gimmicky.

I'm thinking black front (to go with logo), double sided with details on the back, maybe in a different colour?

Logo attached in several different formats.

Front of the card to have logo and added text: People and Development Solutions

Back of the card to also feature logo in some way and say:
Megan Turlow
PO Box (TBA)
Marnoo Flats QLD 4381
0427 318 562
megan@keystonehr-example.com.au
www.keystonehr-example.com.au

Target Market(s)

Small to medium businesses / business owners.

Industry/Entity Type

Marketing

Requirements
Must have
• Double sided business card.
Should not have
• Anything overly gimmicky.

```html
<!DOCTYPE html>
<html lang="en">
<head>
<meta charset="utf-8">
<title>Keystone HR Consulting – Business Card</title>
<link rel="stylesheet" href="https://fonts.googleapis.com/css2?family=Source+Sans+3:wght@300;400;600&family=Cormorant+Garamond:wght@500&display=swap">
<style>
  :root {
    --page-bg: #e4e4e6;
    --card-black: #0a0a0b;
    --card-black-top: #1c1c1e;
    --card-white: #ffffff;
    --ink-dark: #1a1a1a;
    --ink-light: #ffffff;
    --accent-purple: #9a3fd0;
    --band-grey: #3a3a3c;
    --band-dark: #121213;
    --url-grey: #c8c8c8;
    --label-ink: #333333;
  }
  * { margin: 0; padding: 0; box-sizing: border-box; }
  html, body {
    width: 1200px; height: 765px; overflow: hidden;
    background: var(--page-bg);
    font-family: "Source Sans 3", "Myriad Pro", Arial, sans-serif;
  }
  .canvas { position: relative; width: 1200px; height: 765px; }

  .card {
    position: absolute; top: 302px;
    width: 575px; height: 344px;
    border-radius: 44px; overflow: hidden;
  }
  .card--front {
    left: 16px;
    background: linear-gradient(180deg, var(--card-black-top) 0%, var(--card-black) 45%, #000 100%);
  }
  .card--back {
    left: 604px;
    background: var(--card-white);
    border: 1px solid #d6d6d8;
  }

  /* front */
  .brand-dot {
    position: absolute; left: 143px; top: 95px;
    width: 106px; height: 106px; border-radius: 50%;
    background: var(--accent-purple);
  }
  .brand-name {
    position: absolute; left: 272px; top: 128px;
    font-size: 27px; font-weight: 300; color: var(--ink-light);
    white-space: nowrap;
  }
  .tagline {
    position: absolute; left: 272px; top: 192px;
    font-size: 10px; font-weight: 600; letter-spacing: 0.3px;
    color: var(--ink-light); white-space: nowrap;
  }
  .front-band {
    position: absolute; left: 0; top: 265px; width: 100%; height: 15px;
    background: linear-gradient(90deg, var(--band-grey) 0%, #2a2a2c 60%, #6a6a6c 100%);
  }

  /* back */
  .contact {
    position: absolute; right: 90px; top: 152px;
    text-align: right; color: var(--ink-dark);
  }
  .contact__name { font-size: 25px; font-weight: 400; line-height: 1; margin-bottom: 8px; }
  .contact__address { font-size: 12px; line-height: 1.1; }
  .contact__lines { margin-top: 16px; font-size: 12.5px; line-height: 15px; }
  .contact__line { position: relative; }
  .contact__icon {
    position: absolute; right: -24px; top: 2px; width: 13px; height: 11px;
  }
  .back-band {
    position: absolute; left: 0; top: 265px; width: 100%; height: 15px;
    background: var(--band-dark);
  }
  .website {
    position: absolute; right: 90px; top: 265px; height: 15px; line-height: 15px;
    font-size: 9.5px; letter-spacing: 4.6px; color: var(--url-grey);
  }

  .side-label {
    position: absolute; top: 686px;
    font-family: "Cormorant Garamond", Georgia, serif;
    font-size: 15px; letter-spacing: 3px; color: var(--label-ink);
  }
  .side-label--front { left: 66px; }
  .side-label--back { left: 660px; }
</style>
</head>
<body>
<main class="canvas">
  <section class="card card--front" aria-label="Card front">
    <div class="brand-dot"></div>
    <div class="brand-name">Keystone HR Consulting</div>
    <div class="tagline">People and Development Solutions</div>
    <div class="front-band"></div>
  </section>

  <section class="card card--back" aria-label="Card back">
    <div class="contact">
      <div class="contact__name">Megan Turlow</div>
      <div class="contact__address">PO Box (TBA)<br>Marnoo Flats QLD 4381</div>
      <div class="contact__lines">
        <div class="contact__line">0427 318 562
          <svg class="contact__icon" viewBox="0 0 13 11" aria-hidden="true">
            <path d="M1 4 Q6.5 -0.5 12 4 L10.5 5.5 L9 4 L4 4 L2.5 5.5 Z" fill="var(--accent-purple)"/>
            <rect x="2.5" y="6" width="8" height="5" rx="1" fill="var(--accent-purple)"/>
          </svg>
        </div>
        <div class="contact__line">megan@keystonehr-example.com.au
          <svg class="contact__icon" viewBox="0 0 13 11" aria-hidden="true">
            <rect x="0.5" y="1.5" width="12" height="9" rx="1" fill="var(--accent-purple)"/>
            <path d="M1 2 L6.5 6.5 L12 2" fill="none" stroke="#fff" stroke-width="1.2"/>
          </svg>
        </div>
      </div>
    </div>
    <div class="back-band"></div>
    <div class="website">www.keystonehr-example.com.au</div>
  </section>

  <div class="side-label side-label--front">FRONT</div>
  <div class="side-label side-label--back">BACK</div>
</main>
</body>
</html>
```